FenderPals Personal Injury Lawyers Website (Wordpress)

We need a brand new website for our firm's new rebranding. The name of the website is www.fenderpals-example.com. Our new brand will be a group of personal injury lawyers focused on representing only victims in car wrecks. We will be distinguishing ourselves from other law firms due to the fact that other law firms represent clients involving all forms of personal injury. We will only focus on car wrecks and this needs to be reflected on the website.

I have attached the new firm logo and stationary to show the designers the kind of look we are going for in the new website. It needs to be clean, pure, and show the potential clients that we only do one thing and we do it well. That thing is car wrecks.

Some examples of websites that we like are the following:
www.qvt-example.lu - nice interface and colors. nice navigation, we really like the biography pages for the individuals attorneys
www.morvantlegal-example.com - good layout, good navigation
www.pelliardwoss-example.com - navigation bar follows the user whether the user goes up or down

We would like five separate pages -- (1) Home, (2) Client Resources, (3) Expertise / Car Wrecks, (4) Contact Us, (5) News

The Home page will be used for driving traffic and should have a call to action on the right at the top stating that we will send an ebook to anyone who gives their contact information. The ebook will explain how car wrecks work. This should also have room for youtube videos which will be added later.

The client resources will include blogs, books, and information for potential clients. It should be presented in a well developed manner which is both appealing to potential and current clients.

The expertise page will show that we only focus on car wrecks. This needs to be a recurrent theme throughout the entire website. This page will focus on car wrecks and the different aspects including damages, insurance, and investigation.

The Contact Us page will show a google map to our address and phone number. Please use generic information and we will fill in the gaps upon the selection.

News: the news page will show different articles related to past and present cases and the successes of those clients.

The overall page should be elegant and creative. Do not include courthouses, gavels or anything else related to the law. If you include these things, your design will automatically be excluded.
Updates

Please take note this design is now guaranteed. I look forward to receiving everyone's wonderful designs.

Target Market(s)

Persons involved in car wrecks

Industry/Entity Type

Legal

Coding

Coded - Design and coding required

Number of Pages Required

5+ page

Font styles to use
Serif
Sans Serif

Colors
ec1f27
ffffff
000000

Requirements
Must have
• Five pages which focus on representation of car wreck victims. The site must be clean and easy to navigate.
Nice to have
• Navigation bar should follow user up and down the page.
Should not have
• Gavels, court houses, anything related to the law. If your design has these aspects, it will automatically be rejected

```html
<!DOCTYPE html>
<html lang="en">
<head>
<meta charset="utf-8">
<title>FenderPals – Car Wreck Injury Lawyers</title>
<link href="https://fonts.googleapis.com/css2?family=Open+Sans:wght@400;600;700;800&display=swap" rel="stylesheet">
<style>
:root{
  --red:#ec1f27;
  --ink:#000000;
  --charcoal:#2b2b2b;
  --nav:#3a3a3a;
  --dark:#1f1f1f;
  --panel:#262626;
  --grey:#f0f0f0;
  --mid:#8a8a8a;
  --line:#dcdcdc;
  --white:#ffffff;
}
*{box-sizing:border-box;margin:0;padding:0}
html,body{width:700px;height:1200px;overflow:hidden;background:var(--white)}
body{font-family:"Open Sans",Arial,sans-serif;color:var(--charcoal);font-size:7px;line-height:1.45}
.page{width:700px;height:1200px;display:flex;flex-direction:column;overflow:hidden}

/* header */
.site-header{height:44px;flex:none;display:flex;justify-content:space-between;align-items:center;padding:0 32px}
.brand{display:flex;align-items:center;gap:6px}
.brand-mark{width:10px;height:10px;background:var(--red)}
.brand-name{font-size:17px;font-weight:800;color:var(--red);letter-spacing:.5px;text-transform:uppercase}
.header-contact{text-align:right}
.phone{font-size:11px;font-weight:700;color:var(--charcoal)}
.header-row{display:flex;gap:3px;align-items:center;justify-content:flex-end;margin-top:2px;font-size:5.5px;color:var(--mid)}
.social-dot{width:8px;height:8px;border-radius:50%;background:var(--red)}
.social-dot.dark{background:var(--charcoal)}

/* nav */
.main-nav{height:18px;flex:none;background:var(--nav);display:flex;padding:0 32px}
.main-nav a{color:var(--white);text-decoration:none;font-size:5.5px;font-weight:600;text-transform:uppercase;padding:0 11px;line-height:18px;border-right:1px solid #555}
.main-nav a.active{background:var(--red)}

/* hero */
.hero{height:200px;flex:none;position:relative;background:linear-gradient(100deg,#7a2a2e 0%,#d9a1a0 38%,#efe3dc 62%,#c9c3bf 100%)}
.hero-photo{position:absolute;inset:0}
.contact-panel{position:absolute;right:40px;top:22px;width:118px;background:rgba(20,20,20,.85);padding:0 0 8px}
.contact-panel h2{font-size:8.5px;font-weight:600;color:var(--white);padding:8px 9px;border-bottom:1px solid #444;margin-bottom:8px}
.select{margin:0 9px 5px;height:12px;background:var(--white);font-size:5.5px;color:var(--mid);padding:0 4px;line-height:12px;display:flex;justify-content:space-between}
.cta{margin:6px 9px 4px;height:13px;background:var(--red);color:var(--white);font-size:6px;font-weight:700;text-align:center;line-height:13px}
.panel-note{text-align:center;font-size:5px;color:#bbb}

/* media strip */
.media-strip{height:48px;flex:none;background:var(--white);border-bottom:1px solid var(--line);display:flex;align-items:center;justify-content:center;gap:16px}
.media-badge{height:10px;background:#9a9a9a;border-radius:2px}

/* intro */
.intro{height:235px;flex:none;padding:38px 70px 0}
.section-title{font-size:11px;font-weight:700;color:var(--charcoal);text-align:center}
.intro-body{display:flex;gap:22px;margin-top:24px}
.intro-text{flex:1}
.intro-text h3{font-size:10px;font-weight:700;color:var(--red);line-height:1.25;margin-bottom:8px}
.intro-text p{font-size:5.5px;color:#666}
.intro-photo{width:258px;height:110px;background:linear-gradient(120deg,#dcd9d4,#f4f2ee 50%,#b9b2ab)}

/* strengths */
.strengths{height:200px;flex:none;background:var(--grey);padding-top:34px;text-align:center}
.strengths .section-title{width:260px;margin:0 auto;line-height:1.35}
.strength-list{display:flex;justify-content:center;gap:44px;margin-top:24px}
.strength{width:72px;display:flex;flex-direction:column;align-items:center;gap:8px}
.strength-icon{width:32px;height:32px;border-radius:50%;background:var(--charcoal);display:flex;align-items:center;justify-content:center}
.strength-icon.accent{background:var(--red)}
.strength span{font-size:6px;font-weight:600;color:var(--charcoal)}

/* compensation */
.compensation{height:228px;flex:none;padding:30px 120px 0}
.compensation .section-title{width:260px;margin:0 auto;line-height:1.35}
.compensation-body{display:flex;gap:22px;margin-top:24px}
.benefit-list{list-style:none;width:118px}
.benefit-list li{height:20px;border:1px solid var(--line);margin-bottom:6px;display:flex;align-items:center;font-size:6px;font-weight:600}
.benefit-list li::before{content:"";width:16px;height:18px;background:var(--nav);margin-right:7px;
  background-image:linear-gradient(45deg,transparent 45%,var(--white) 45%,var(--white) 55%,transparent 55%)}
.consult-box{flex:1;background:var(--panel);padding:12px 14px;color:#d8d8d8}
.consult-box h4{color:var(--red);font-size:7px;text-align:center;border-bottom:1px solid #444;padding-bottom:7px;margin-bottom:8px;text-transform:uppercase}
.consult-box p{font-size:5.5px;margin-bottom:8px}
.consult-box .talk{font-size:6px;font-weight:700;color:var(--white)}
.consult-box .talk em{color:var(--red);font-style:normal}

/* footer */
.site-footer{flex:1;background:var(--dark);color:#bdbdbd;display:flex;flex-direction:column}
.tweet-bar{height:56px;border-bottom:1px solid #333;display:flex;align-items:center;padding:0 120px;gap:10px}
.tweet-mark{width:16px;height:16px;border-radius:50%;background:#3aa3e0}
.tweet-text{flex:1;font-size:5.5px}
.tweet-text strong{display:block;color:var(--white);font-size:7px}
.tweet-text em{color:var(--red);font-style:normal}
.footer-social{display:flex;gap:4px}
.footer-social span{width:12px;height:12px;background:#3b3b3b}
.footer-cols{display:flex;gap:24px;padding:20px 120px 0;flex:1}
.footer-col h5{color:var(--white);font-size:7px;margin-bottom:6px}
.footer-col ul{list-style:none;font-size:5.5px}
.footer-col li{margin-bottom:3px}
.footer-col li::before{content:"› ";color:var(--red)}
.newsletter{width:140px}
.newsletter p{font-size:5.5px;margin-bottom:6px}
.newsletter-field{display:flex;height:12px}
.newsletter-field span{flex:1;background:var(--white);font-size:5px;color:var(--mid);padding-left:4px;line-height:12px}
.newsletter-field b{width:22px;background:var(--red)}
.rating-badge{width:82px;height:28px;background:#4a4a4a;border-radius:2px;margin-top:4px}
.copyright{padding:0 0 12px;text-align:center;font-size:5px;color:#777}
</style>
</head>
<body>
<div class="page">

  <header class="site-header">
    <div class="brand"><span class="brand-mark"></span><span class="brand-name">FenderPals</span></div>
    <div class="header-contact">
      <div class="phone">(305) 555-0142</div>
      <div class="header-row">Call us today – free case review
        <span class="social-dot dark"></span><span class="social-dot"></span><span class="social-dot"></span><span class="social-dot"></span></div>
    </div>
  </header>

  <nav class="main-nav">
    <a href="#">Home</a><a href="#">Our Firm</a><a href="#" class="active">Car Wrecks</a><a href="#">Client Resources</a><a href="#">Injury Types</a><a href="#">Case Results</a><a href="#">News</a><a href="#">Contact Us</a>
  </nav>

  <section class="hero">
    <div class="hero-photo" role="img" aria-label="Photograph of a client seated at a desk in a bright office, warm red tones"></div>
    <form class="contact-panel">
      <h2>Contact a lawyer now</h2>
      <div class="select">Your name <span>▾</span></div>
      <div class="select">Case type <span>▾</span></div>
      <div class="cta">Free Consultation</div>
      <div class="panel-note">No fee unless we win</div>
    </form>
  </section>

  <section class="media-strip" aria-label="As featured in">
    <span class="media-badge" style="width:28px"></span>
    <span class="media-badge" style="width:22px;height:16px"></span>
    <span class="media-badge" style="width:36px"></span>
    <span class="media-badge" style="width:40px;height:8px"></span>
    <span class="media-badge" style="width:30px"></span>
    <span class="media-badge" style="width:50px;height:8px"></span>
    <span class="media-badge" style="width:30px;height:14px"></span>
  </section>

  <section class="intro">
    <h2 class="section-title">Nationally Recognized Car Wreck Injury Lawyers</h2>
    <div class="intro-body">
      <div class="intro-text">
        <h3>Come to us for a fair legal recovery after your car wreck</h3>
        <p>Our team works only with people hurt in car wrecks. We study every claim closely, deal with the insurers for you and push for the full recovery you deserve. From the first call to the final check, you will always know where your case stands and who is handling it.</p>
      </div>
      <div class="intro-photo" role="img" aria-label="Photograph of a lawyer meeting with two clients"></div>
    </div>
  </section>

  <section class="strengths">
    <h2 class="section-title">Skilled car wreck lawyers with an extensive record of legal victories</h2>
    <div class="strength-list">
      <div class="strength"><div class="strength-icon"><svg width="14" height="14" viewBox="0 0 14 14"><circle cx="7" cy="5" r="4" fill="none" stroke="#fff" stroke-width="1.5"/><path d="M4 8l-1 5 4-2 4 2-1-5" fill="none" stroke="#fff" stroke-width="1.2"/></svg></div><span>Outstanding credentials</span></div>
      <div class="strength"><div class="strength-icon accent"><svg width="14" height="14" viewBox="0 0 14 14"><circle cx="7" cy="4" r="3" fill="#fff"/><path d="M1 14c0-4 3-6 6-6s6 2 6 6z" fill="#fff"/></svg></div><span>Individualized attention</span></div>
      <div class="strength"><div class="strength-icon"><svg width="14" height="14" viewBox="0 0 14 14"><path d="M5 1h4v4h4v4H9v4H5V9H1V5h4z" fill="#fff"/></svg></div><span>Exceptional medical expertise</span></div>
      <div class="strength"><div class="strength-icon"><svg width="14" height="14" viewBox="0 0 14 14"><path d="M2 7l3 3 7-7" fill="none" stroke="#fff" stroke-width="2"/></svg></div><span>A history of success</span></div>
    </div>
  </section>

  <section class="compensation">
    <h2 class="section-title">Car wreck lawyers who obtain your rightful compensation</h2>
    <div class="compensation-body">
      <ul class="benefit-list">
        <li>Outstanding credentials</li>
        <li>Individualized attention</li>
        <li>Exceptional medical expertise</li>
        <li>A history of success</li>
      </ul>
      <div class="consult-box">
        <h4>Free case evaluation</h4>
        <p>After a wreck, the days that follow matter most. Our lawyers look at the facts, the medical records and the policy limits so nothing is missed. We answer your questions in plain words and never charge a fee unless we win your case.</p>
        <p>Call now or send us a short message and a member of our team will reach you within one business day.</p>
        <div class="talk">Talk with one of our lawyers <em>for free »</em></div>
      </div>
    </div>
  </section>

  <footer class="site-footer">
    <div class="tweet-bar">
      <span class="tweet-mark"></span>
      <div class="tweet-text"><strong>Latest tweet</strong>Just posted: five steps to take right after a car wreck <em>@fenderpals_law</em></div>
      <div class="footer-social"><span></span><span></span><span></span></div>
    </div>
    <div class="footer-cols">
      <div class="footer-col"><h5>Main Menu</h5><ul><li>Home</li><li>Our Firm</li><li>Car Wrecks</li><li>News</li><li>Contact</li></ul></div>
      <div class="footer-col"><h5>Useful Link</h5><ul><li>Client Resources</li><li>Free Ebook</li><li>Case Results</li><li>Site Map</li></ul></div>
      <div class="footer-col newsletter"><h5>Newsletter</h5><p>Sign up for safety tips and news from our team.</p><div class="newsletter-field"><span>Your email</span><b></b></div></div>
      <div class="rating-badge"></div>
    </div>
    <div class="copyright">© FenderPals. All rights reserved.</div>
  </footer>

</div>
</body>
</html>
```